Bright Harbor Health (03)

We're designing a website to sell Medicare Supplements. Attached is the script we want to say and general layout, but please use your best knowledge to make it better. This platform should be extremely user-friendly, but we want to make it look fun and approachable! Most Insurance/medicare websites are very boring, drab, simple but we want this one to be more personalized, fun and sexy (but again, still user-friendly since our target demographic is 65+).

This homepage should include a fun and inviting quiz, the script is in the attachment below. It should also include the blurbs about what medicare supplements plans are and why they should buy them. Feel free to play around with cool fonts and imagery, we want the site to be engaging!

Target Market(s)

seniors

Industry/Entity Type

Insurance

Number of Pages Required

1 page

Requirements
Must have
• Quiz, company name and tag line, script
Nice to have
• fun, engaging elements

```html
<!DOCTYPE html>
<html lang="en">
<head>
<meta charset="utf-8">
<title>Bright Harbor Health</title>
<link href="https://fonts.googleapis.com/css2?family=Roboto:wght@400;500;700&family=Open+Sans:wght@400;600&display=swap" rel="stylesheet">
<style>
:root{
  --teal:#0f6b5c;
  --red:#ef3157;
  --brown:#8c6e4e;
  --dark:#1c2a2f;
  --ink:#222;
  --sand:#eeebe6;
  --faq:#efefef;
}
*{box-sizing:border-box;margin:0;padding:0}
html,body{width:1200px;height:2872px;overflow:hidden}
body{font-family:Roboto,sans-serif;color:var(--ink);background:#fff;position:relative}
.abs{position:absolute}
.center{text-align:center}
.h2{font-weight:700;color:var(--teal);font-size:32px;line-height:40px}
.rule{position:absolute;height:3px;width:80px;background:var(--brown)}
.btn{position:absolute;background:var(--red);color:#fff;font-weight:700;font-size:13px;border-radius:22px;display:flex;align-items:center;justify-content:center}
.pill{position:absolute;background:var(--teal);color:#fff;font-size:12px;border-radius:14px;display:flex;align-items:center;justify-content:center;width:89px;height:27px}
.logo{font-family:"Open Sans",sans-serif;font-weight:600;font-size:42px;line-height:42px;color:var(--dark);letter-spacing:-.3px}
.tag{font-family:"Open Sans",sans-serif;font-weight:600;font-size:10px;color:var(--teal)}
/* header */
.nav{font-size:16px;color:var(--teal);font-weight:500}
.phone{left:896px;top:0;width:210px;height:126px;background:var(--red);color:#fff;font-size:21px;font-weight:500;display:flex;align-items:center;justify-content:center;gap:10px}
/* hero */
.hero-photo{left:0;top:126px;width:762px;height:287px;background:linear-gradient(100deg,#4d6a4a,#8aa27c 40%,#b8c6b0 60%,#5b6d5e)}
.hero-side{left:762px;top:126px;width:438px;height:287px;background:linear-gradient(90deg,#dfeedd,#d5ebd0)}
.quote-box{background:var(--dark);color:#fff;border-radius:4px}
.quote-title{font-weight:700;font-size:27px;line-height:32px}
.pin-field{position:absolute;background:#fff;display:flex;align-items:center;gap:10px;font-size:26px;color:#555;padding-left:36px}
.tabs{left:0;top:413px;width:1200px;height:67px;background:var(--dark)}
.tab{position:absolute;top:0;height:67px;width:328px;color:#fff;font-size:15px;font-weight:500;display:flex;align-items:center;justify-content:center;gap:8px}
/* benefits */
.benefit{position:absolute;width:260px;text-align:center}
.bignum{position:absolute;font-size:200px;font-weight:700;color:#f1ede8;line-height:1}
.benefit h3{color:var(--red);font-size:19px;font-weight:500;margin-top:0}
.benefit p{font-size:13px;line-height:16px;margin-top:14px;color:#333}
.link-line{position:absolute;top:758px;height:1px;width:75px;background:#ddd}
/* how */
.how{left:0;top:926px;width:1200px;height:367px;background:linear-gradient(90deg,#e3e6ea,#f5f6f7 35%,#eceef0 60%,#f4f4f5)}
.part{position:absolute;width:200px;text-align:center}
.part b{display:block;color:var(--red);font-size:19px;font-weight:500}
.part span{display:block;font-size:13px;font-weight:500;line-height:16px;margin-top:4px;color:#222}
/* faq */
.faq{position:absolute;left:623px;width:483px;height:36px;background:var(--faq);font-size:15px;display:flex;align-items:center;justify-content:space-between;padding:0 18px}
.faq i{font-style:normal;color:var(--red);font-size:16px}
/* blog */
.blog{left:0;top:1765px;width:1200px;height:710px;background:var(--sand)}
.card{position:absolute;top:1911px;width:323px}
.card .img{height:231px}
.card .meta{height:33px;background:var(--red);color:#fff;font-size:14px;display:flex;align-items:center;padding-left:12px}
.card h4{color:var(--teal);font-size:17px;font-weight:500;margin-top:21px}
.card p{font-size:13.4px;line-height:21.4px;color:#444;margin-top:6px}
/* footer */
.footer{left:0;top:2475px;width:1200px;height:301px;background:var(--dark);color:#fff}
.foot-h{position:absolute;top:50px;font-size:17px;font-weight:500;color:#c8a27a}
.foot-list{position:absolute;list-style:none}
.foot-list li{display:flex;gap:14px;align-items:center}
.copy{left:0;top:2776px;width:1200px;height:96px;background:var(--teal);color:#fff;font-size:13px;display:flex;align-items:center;justify-content:center}
</style>
</head>
<body>

<!-- header -->
<div class="abs" style="left:96px;top:34px">
  <div class="logo">Bright Harbor Health</div>
  <div class="tag">Be confident in choosing the Medicare Supplement plan that's right for you.</div>
</div>
<div class="abs nav" style="left:558px;top:51px">Supplements List ▾</div>
<div class="abs nav" style="left:726px;top:49px;font-size:21px;display:flex;gap:12px;align-items:center">
  <svg width="14" height="14" viewBox="0 0 14 14"><circle cx="7" cy="7" r="6" fill="none" stroke="#1c2a2f" stroke-width="2"/><path d="M3 7a4 4 0 0 1 8 0" fill="#1c2a2f"/></svg>Live Support</div>
<div class="abs phone">
  <svg width="18" height="18" viewBox="0 0 24 24"><path fill="#fff" d="M6.6 10.8a15 15 0 0 0 6.6 6.6l2.2-2.2c.3-.3.7-.4 1-.2 1.1.4 2.3.6 3.6.6.6 0 1 .4 1 1V20c0 .6-.4 1-1 1A17 17 0 0 1 3 4c0-.6.4-1 1-1h3.5c.6 0 1 .4 1 1 0 1.3.2 2.5.6 3.6.1.3 0 .7-.2 1z"/></svg>(800) 555-0142</div>

<!-- hero -->
<div class="abs hero-photo" role="img" aria-label="Photo of two smiling senior men, one on a phone and one using a tablet"></div>
<div class="abs hero-side"></div>
<div class="abs quote-box" style="left:762px;top:144px;width:344px;height:252px">
  <div class="quote-title center" style="margin-top:26px">Find Your 2020<br>Medicare Plan</div>
  <div class="pin-field" style="left:31px;top:113px;width:283px;height:48px">
    <svg width="14" height="20" viewBox="0 0 14 20"><path fill="#222" d="M7 0a7 7 0 0 0-7 7c0 5 7 13 7 13s7-8 7-13a7 7 0 0 0-7-7zm0 10a3 3 0 1 1 0-6 3 3 0 0 1 0 6z"/></svg>Enter Pincode</div>
  <div class="btn" style="left:95px;top:180px;width:150px;height:41px">Get FREE Quotes</div>
</div>
<div class="abs tabs">
  <div class="tab" style="left:95px;background:var(--teal)"><svg width="14" height="14"><circle cx="7" cy="7" r="6" fill="none" stroke="#fff" stroke-width="1.8"/><circle cx="7" cy="7" r="2.5" fill="#fff"/></svg>Medicare Supplement</div>
  <div class="tab" style="left:437px;background:var(--red)"><svg width="14" height="14"><circle cx="7" cy="7" r="6" fill="none" stroke="#fff" stroke-width="1.8"/><circle cx="7" cy="7" r="2.5" fill="#fff"/></svg>Medicare Part D</div>
  <div class="tab" style="left:779px;background:var(--brown)"><svg width="14" height="14"><circle cx="7" cy="7" r="6" fill="none" stroke="#fff" stroke-width="1.8"/><circle cx="7" cy="7" r="2.5" fill="#fff"/></svg>Medicare Advantage</div>
</div>

<!-- benefits -->
<div class="abs h2 center" style="left:0;top:520px;width:1200px">Understanding The Benefits<br>of Medicare Insurance</div>
<div class="rule" style="left:560px;top:620px"></div>

<div class="bignum" style="left:185px;top:650px">1</div>
<div class="bignum" style="left:530px;top:650px">2</div>
<div class="bignum" style="left:880px;top:650px">3</div>
<div class="link-line" style="left:388px"></div>
<div class="link-line" style="left:731px"></div>

<svg class="abs" style="left:222px;top:691px" width="64" height="64" viewBox="0 0 64 64"><rect width="64" height="64" rx="4" fill="#8c6e4e"/><path d="M14 33l12 12 24-26" stroke="#fff" stroke-width="7" fill="none"/></svg>
<svg class="abs" style="left:580px;top:691px" width="40" height="66" viewBox="0 0 40 66"><g fill="none" stroke="#8c6e4e" stroke-width="4"><path d="M2 3h36M2 63h36M6 3c0 20 28 22 28 30S6 43 6 63M34 3c0 20-28 22-28 30s28 10 28 30"/></g><path d="M12 58h16l-8-10z" fill="#8c6e4e"/></svg>
<svg class="abs" style="left:913px;top:691px" width="68" height="66" viewBox="0 0 68 66"><g fill="none" stroke="#8c6e4e" stroke-width="3.5"><path d="M4 2h40v60H4z"/><path d="M12 14h26M12 24h26M12 34h18M12 44h14"/><circle cx="46" cy="46" r="16" fill="#fff"/><path d="M38 50l12-12 4 4-12 12h-4z"/></g></svg>

<div class="benefit" style="left:123px;top:777px"><h3>FREE to Use</h3><p>Lorem Ipsum is simply dummy text of the printing and typesetting industry. Lorem Ipsum has been the industry's standard dummy text ever since the 1500s.</p></div>
<div class="benefit" style="left:470px;top:777px"><h3>We help you save time</h3><p>Lorem Ipsum is simply dummy text of the printing and typesetting industry. Lorem Ipsum has been the industry's standard dummy text ever since the 1500s.</p></div>
<div class="benefit" style="left:816px;top:777px"><h3>Plan recommendation</h3><p>Lorem Ipsum is simply dummy text of the printing and typesetting industry. Lorem Ipsum has been the industry's standard dummy text ever since the 1500s.</p></div>

<!-- how medicare works -->
<div class="abs how" role="img" aria-label="Faded background photo of a doctor talking with a senior patient"></div>
<div class="btn" style="left:1043px;top:906px;width:180px;height:42px;border-radius:22px 0 0 22px;justify-content:flex-start;padding-left:33px">Get FREE Quotes</div>
<div class="abs h2 center" style="left:0;top:970px;width:1200px">How Medicare works</div>
<div class="rule" style="left:560px;top:1030px"></div>

<svg class="abs" style="left:173px;top:1073px" width="42" height="54" viewBox="0 0 42 54"><rect x="2" y="6" width="38" height="48" fill="#8c6e4e"/><rect x="14" y="0" width="14" height="10" fill="#8c6e4e"/><g fill="#fff"><rect x="8" y="14" width="6" height="6"/><rect x="18" y="14" width="6" height="6"/><rect x="28" y="14" width="6" height="6"/><rect x="8" y="26" width="6" height="6"/><rect x="18" y="26" width="6" height="6"/><rect x="28" y="26" width="6" height="6"/><rect x="17" y="40" width="8" height="14"/></g></svg>
<svg class="abs" style="left:373px;top:1073px" width="42" height="54" viewBox="0 0 42 54"><path fill="#8c6e4e" d="M21 0C9 0 2 9 2 20c0 8 4 12 4 18v16h24v-8h6c3 0 4-2 4-5v-6l2-2-3-8C38 11 33 0 21 0z"/><circle cx="18" cy="22" r="7" fill="none" stroke="#fff" stroke-width="3"/></svg>
<svg class="abs" style="left:584px;top:1073px" width="32" height="56" viewBox="0 0 32 56"><path fill="#8c6e4e" d="M0 0h32v6h-4v34a12 12 0 0 1-24 0V6H0z"/><path fill="#fff" d="M10 10h4v28h-4zM18 10h4v28h-4z"/></svg>
<svg class="abs" style="left:788px;top:1073px" width="52" height="50" viewBox="0 0 52 50"><path fill="#8c6e4e" d="M16 0h20v10h12a4 4 0 0 1 4 4v32a4 4 0 0 1-4 4H4a4 4 0 0 1-4-4V14a4 4 0 0 1 4-4h12zm4 4v6h12V4z"/><path fill="#fff" d="M22 18h8v8h8v8h-8v8h-8v-8h-8v-8h8z"/></svg>
<svg class="abs" style="left:998px;top:1073px" width="46" height="56" viewBox="0 0 46 56"><path fill="#8c6e4e" d="M0 0h46v26c0 16-12 26-23 30C12 52 0 42 0 26z"/><path fill="#fff" d="M12 6h6v38c-4-3-6-8-6-14z"/></svg>

<div class="part" style="left:92px;top:1137px"><b>Part A</b><span>Hospital &amp; Inpatient</span></div>
<div class="part" style="left:293px;top:1137px"><b>Part B</b><span>Doctors &amp; Medical</span></div>
<div class="part" style="left:500px;top:1137px"><b>Part C</b><span>Medicare Advantage</span></div>
<div class="part" style="left:714px;top:1137px"><b>Part D</b><span>Medicare Prescription<br>Drug Coverage</span></div>
<div class="part" style="left:920px;top:1137px"><b>Part E</b><span>Supplement also called<br>Bright Harbor Health</span></div>

<div class="pill" style="left:148px;top:1215px">Learn More</div>
<div class="pill" style="left:349px;top:1215px">Learn More</div>
<div class="pill" style="left:556px;top:1215px">Learn More</div>
<div class="pill" style="left:770px;top:1215px">Learn More</div>
<div class="pill" style="left:980px;top:1215px">Learn More</div>

<!-- quote + faq -->
<div class="abs h2" style="left:95px;top:1336px">Get a Free Medicare Quote</div>
<div class="rule" style="left:96px;top:1396px"></div>
<div class="abs h2" style="left:622px;top:1336px">Frequently Asked Questions</div>
<div class="rule" style="left:624px;top:1396px"></div>

<div class="abs quote-box" style="left:96px;top:1440px;width:481px;height:273px">
  <div class="quote-title" style="margin:26px 0 0 33px">Find Your 2020<br>Medicare Plan</div>
  <div class="pin-field" style="left:35px;top:113px;width:283px;height:48px;padding-left:12px">
    <svg width="14" height="20" viewBox="0 0 14 20"><path fill="#222" d="M7 0a7 7 0 0 0-7 7c0 5 7 13 7 13s7-8 7-13a7 7 0 0 0-7-7zm0 10a3 3 0 1 1 0-6 3 3 0 0 1 0 6z"/></svg>Enter Pincode</div>
  <div class="btn" style="left:35px;top:180px;width:150px;height:41px">Get FREE Quotes</div>
</div>

<div class="faq" style="top:1440px">What is Medigap Insurance?<i>+</i></div>
<div class="faq" style="top:1488px">Important Fact: How to Save Money!<i>+</i></div>
<div class="faq" style="top:1536px">Where Do I Purchase Medigap Insurance?<i>+</i></div>
<div class="faq" style="top:1584px">When Can I Sign Up for Medigap Insurance?<i>+</i></div>
<div class="faq" style="top:1632px">Who is Eligible for Medigap Insurance?<i>+</i></div>
<div class="faq" style="top:1680px">Who Purchases Medigap Insurance?<i>+</i></div>

<!-- blog -->
<div class="abs blog"></div>
<div class="abs h2 center" style="left:0;top:1808px;width:1200px">Recently Written By Our Insurance Experts</div>
<div class="rule" style="left:560px;top:1866px"></div>

<div class="card" style="left:95px">
  <div class="img" role="img" aria-label="Photo of a senior couple jogging outdoors under a blue sky" style="background:linear-gradient(180deg,#6fa6d6,#a9cde6 60%,#6a8a4a)"></div>
  <div class="meta"><b>Updated:</b>&nbsp;March 10, 2020 | 5 min read</div>
  <h4>Memory Exercises For Seniors</h4>
  <p>With older age comes the steady decline of brain function and cognitive ability. Losing some cognitive function is normal for seniors, but there are ways to prevent its most severe effects. One of the most affected brain functions in seniors is memory. Memory impairment is a natural occurrence for an aging brain, but decades of...</p>
</div>
<div class="card" style="left:439px">
  <div class="img" role="img" aria-label="Photo of a cheerful senior couple holding cash" style="background:linear-gradient(120deg,#d9d4cc,#efe9e0 45%,#c7b7a0)"></div>
  <div class="meta"><b>Updated:</b>&nbsp;March 10, 2020 | 5 min read</div>
  <h4>Ways for Seniors to Save Money</h4>
  <p>Are you looking to save more money and achieve financial stability? Lucky for you, there are several different ways in which you can cut your costs and maximize your savings. For any seniors looking to retire, the last thing you want on your mind is worrying about your money. Through proper budgeting, lifestyle changes, and...</p>
</div>
<div class="card" style="left:783px">
  <div class="img" role="img" aria-label="Photo of a doctor visiting a senior patient in a hospital bed" style="background:linear-gradient(100deg,#c9d0d4,#e8eaec 50%,#b9c0c6)"></div>
  <div class="meta"><b>Updated:</b>&nbsp;March 10, 2020 | 5 min read</div>
  <h4>Medicare and VA Benefits</h4>
  <p>If you are eligible for Medicare and are a veteran, you may apply for more benefits through Veteran Affair (VA) plans. The VA plans give more opportunities for healthcare and may be used in addition to Medicare, but are completely separate from Medicare. One big difference between the two benefits are the locations that they...</p>
</div>
<div class="pill" style="left:96px;top:2397px">Learn More</div>
<div class="pill" style="left:439px;top:2397px">Learn More</div>
<div class="pill" style="left:783px;top:2397px">Learn More</div>

<!-- footer -->
<div class="abs footer">
  <div class="abs" style="left:95px;top:46px">
    <div class="logo" style="color:#fff">Bright Harbor Health</div>
    <div class="tag" style="color:#fff">Be confident in choosing the Medicare Supplement plan that's right for you.</div>
  </div>
  <p class="abs" style="left:96px;top:132px;width:470px;font-size:13.4px;line-height:21.4px;color:#e4e8ea">Lorem ipsum dolor sit amet, consectetur adipiscing elit. Fusce sed facilisis metus, ut mollis tortor. Proin sit amet nisi placerat, rutrum massa ut, consequat felis. Vivamus finibus lobortis orci vel hendrerit. Ut convallis vulputate massa, eget vehicula velit facilisis eu. In eleifend odio libero, non commodo quam euismod pellentesque. Morbi mattis dui eu ante placerat feugiat. Proin vitae magna eu ipsum lobortis faucibus non vel nunc.</p>
  <div class="foot-h" style="left:671px">Useful Links</div>
  <div class="rule" style="left:671px;top:88px;width:58px;height:2px"></div>
  <ul class="foot-list" style="left:677px;top:130px;font-size:14px;line-height:33px;color:#e4e8ea">
    <li><span style="color:#c8a27a">–</span>Home</li>
    <li><span style="color:#c8a27a">–</span>Categories</li>
    <li><span style="color:#c8a27a">–</span>How it works</li>
    <li><span style="color:#c8a27a">–</span>T&amp;C</li>
  </ul>
  <div class="foot-h" style="left:878px">How to Reach</div>
  <div class="rule" style="left:878px;top:88px;width:58px;height:2px"></div>
  <ul class="foot-list" style="left:878px;top:128px;font-family:'Open Sans',sans-serif;font-weight:600;font-size:22px;line-height:26px">
    <li style="margin-bottom:13px"><span style="color:#c8a27a">–</span>Call (800) 555-0142</li>
    <li style="margin-bottom:13px"><span style="color:#c8a27a">–</span>Live Support</li>
    <li style="align-items:flex-start"><span style="color:#c8a27a">–</span>Address #41 lorem<br>ipsum, dolor</li>
  </ul>
</div>
<div class="abs copy">Copyright © 2020. All Rights Reserved</div>

</body>
</html>
```